Website for Arts Studios including Audio, Video and Performing Arts

Creating an engaging and informative website for Brightwell Studios is a paramount endeavor that demands careful consideration of the brand's identity, values, and goals. This project offers a unique opportunity to showcase the studio's multifaceted offerings and establish a strong online presence. In order to fulfill the objectives outlined in the website brief, we will design a comprehensive, user-friendly, and aesthetically pleasing website that not only introduces Brightwell Studios to the world but also provides a seamless experience for visitors.

The website's primary focus is to present Brightwell Studios as a hub for creativity, wellness, and community engagement. To achieve this, we will construct various sections that highlight the studio's features and appeal to a broad audience:

1. **Classes and Studio Sessions**: A central element of the website will be dedicated to showcasing the various classes and studio sessions offered by Brightwell Studios. This section will provide detailed information about the classes available, their schedules, and the instructors, encouraging visitors to explore and sign up for sessions that align with their interests and needs.

2. **About Section**: This segment will provide an in-depth insight into the ethos and history of Brightwell Studios. It will introduce the founders, their vision, and the core values that underpin the studio's operations. We will incorporate compelling storytelling and visuals to create a strong emotional connection with visitors.

3. **Staffing Section**: Highlighting the talented and dedicated team behind Brightwell Studios is crucial. This section will include profiles of instructors, trainers, and support staff, enabling visitors to get to know the individuals who make the studio a vibrant and welcoming place.

4. **Phases Description**: To communicate the studio's growth and evolution, we will incorporate a section outlining the different phases of development. Phase 1, Phase 2, and future phases will be described, giving visitors a clear understanding of Brightwell Studios' ongoing commitment to innovation and expansion.

5. **Contact Us**: A user-friendly contact section will be integrated to facilitate easy communication between Brightwell Studios and its audience. Visitors can inquire about classes, studio bookings, or any other inquiries, fostering a sense of accessibility and approachability.

In addition to these core sections, the website will also prioritize responsive design and easy navigation, ensuring that users can access the information they seek on various devices and screen sizes. We will focus on creating a visually appealing and cohesive design, using a color palette and imagery that aligns with the studio's branding.

In conclusion, the website we propose for Brightwell Studios goes beyond being a mere online presence; it serves as a dynamic platform to introduce the studio to the world. By combining compelling content, user-friendly features, and a commitment to capturing the essence of Brightwell Studios, our design will help the studio engage with a global audience, promote its mission, and foster a sense of belonging among its visitors.

Target Market(s)

Artists in the DFW metroplec

Industry/Entity Type

Entertainment/Music/Performing Arts

Coding

Coded - Design and coding required

Number of Pages Required

1 page

Font styles to use
Other font styles liked:
• Cachet should be included within the font set.

Colors
FFC000
F8CF3A
FAE287
FDF2CF
FEFAEE

Requirements
Must have
• The sections in the description
Nice to have
• A floating video in the background of the landing page
Should not have
• any ecommerce bits

```html
<!DOCTYPE html>
<html lang="en">
<head>
<meta charset="utf-8">
<title>Brightwell Studios – Phase I</title>
<link href="https://fonts.googleapis.com/css2?family=Fira+Sans+Condensed:wght@300;400;500&family=Allison&family=Oswald:wght@500&display=swap" rel="stylesheet">
<style>
:root{
  --ink:#000;
  --paper:#fff;
  --gold:#FFC000;
  --gold-soft:#F8CF3A;
  --text:#2b2b2b;
  --portrait:#8a8a8a;
  --rule:#e8e8e8;
}
*{margin:0;padding:0;box-sizing:border-box}
html,body{width:1200px;height:2625px;overflow:hidden}
body{position:relative;background:var(--paper);font-family:"Fira Sans Condensed",sans-serif;font-weight:300;color:var(--text)}
.abs{position:absolute}
/* header */
.site-header{left:0;top:0;width:1200px;height:215px;background:radial-gradient(ellipse at 62% 40%,#3a3a3a 0%,#1a1a1a 35%,#000 70%)}
.brand-name{color:var(--paper);font-weight:400;font-size:36px;line-height:1;white-space:nowrap}
.brand-sub{left:210px;top:137px;color:var(--paper);font-size:14px;line-height:17px;font-weight:300}
.nav{display:flex;gap:40px;font-size:13px;font-weight:400;text-transform:uppercase;color:var(--paper)}
.nav .current{color:var(--gold);font-weight:500}
.crumbs{left:163px;top:261px;font-size:13px;font-weight:300;color:var(--text)}
.crumbs .here{color:var(--gold);font-size:12px;font-weight:500}
.crumb-rule{left:0;top:288px;width:1200px;height:1px;background:var(--rule)}
/* titles */
.script-title{width:1200px;left:0;text-align:center;font-family:"Allison",cursive;font-weight:400;font-size:72px;color:var(--ink);line-height:1}
/* intro */
.intro-photo{left:161px;top:459px;width:400px;height:264px;background:radial-gradient(ellipse at 70% 25%,#ff1e38 0%,#c8183a 30%,#7a2a45 65%,#4a2a38 100%)}
.intro-frame{left:169px;top:467px;width:400px;height:264px;border:1px solid var(--gold)}
.facts{left:603px;top:450px;width:430px;list-style:none;font-size:13px;line-height:21.5px}
.facts li{position:relative;padding-left:15px;margin-bottom:10.5px}
.facts li::before{content:"";position:absolute;left:0;top:7px;border-left:7px solid var(--gold);border-top:4px solid transparent;border-bottom:4px solid transparent}
.facts b{color:var(--gold);font-weight:500}
/* team */
.player{width:280px}
.player-photo{width:264px;height:282px;border-radius:28px;background:linear-gradient(180deg,#9a9a9a,#6e6e6e)}
.player-name{margin-top:24px;font-family:"Oswald",sans-serif;font-weight:500;font-variant:small-caps;font-size:28px;line-height:1;color:var(--ink)}
.player-role{margin-top:14px;font-size:13.5px;font-weight:300;color:var(--text)}
.player-role.small{font-size:9px;margin-top:16px}
/* footer */
.footer-body{left:0;top:2365px;width:1200px;height:260px;background:var(--ink)}
.footer-nav{left:486px;top:2440px;width:553px;display:flex;justify-content:space-between;font-size:12.5px;text-transform:uppercase;color:var(--paper);font-weight:400}
.footer-nav .current{color:var(--gold);font-weight:500}
.footer-rule{left:488px;top:2479px;width:551px;height:1px;background:#444}
.contact{display:flex;gap:12px;align-items:center;color:var(--paper);font-size:13.5px;line-height:20px;font-weight:300}
.contact .big{font-size:14.5px}
.socials{left:891px;top:2502px;display:flex;gap:7px}
.socials span{width:32px;height:32px;border:1px solid #bbb;border-radius:50%}
.copyright-rule{left:0;top:2578px;width:1200px;height:1px;background:#333}
.copyright{left:0;top:2593px;width:1200px;text-align:center;color:var(--paper);font-size:13px;font-weight:300}
</style>
</head>
<body>

<header class="site-header abs" role="img" aria-label="Dark monochrome photo of a dancer in motion"></header>
<div class="brand-name abs" style="left:162px;top:55px">Brightwell Studios</div>
<p class="brand-sub abs">An initiative of the<br>Harborline Community Trust</p>
<nav class="nav abs" style="left:639px;top:37px">
  <span>Home</span><span>About</span><span>Booking</span><span class="current">Phase I</span><span>Future Phases</span>
</nav>

<div class="crumbs abs">Home &nbsp;»&nbsp; <span class="here">Phase I</span></div>
<div class="crumb-rule abs"></div>

<h1 class="script-title abs" style="top:335px">Phase I</h1>

<div class="intro-frame abs"></div>
<div class="intro-photo abs" role="img" aria-label="Saxophonist performing in red stage smoke"></div>
<ul class="facts abs">
  <li>90 days ago this was a racquetball court</li>
  <li>Now it is a full-fledged teaching studio</li>
  <li><b>Full Fledged:</b> Means any budding or big-time artist would want to use this space that has top-of-the-line gear, acoustic treatment, and amenities</li>
  <li><b>Teaching Studio:</b> Equipped with 6 learning lab production stations for learning and immediate application</li>
  <li>Imagine a place that immerses young people from elementary school ages up in music tech education, serves as a workforce development and certification hub for teens and young adults and provides world class services to artists near and far - that's the epitome of Brightwell Studios.</li>
  <li>This is <b>Phase 1:</b> music recording studio</li>
</ul>

<h2 class="script-title abs" style="top:838px">Key Players</h2>

<article class="player abs" style="left:161px;top:975px">
  <div class="player-photo" role="img" aria-label="Black-and-white portrait of Marcus Dale"></div>
  <h3 class="player-name">Marcus Dale</h3><p class="player-role">Project Coordinator</p>
</article>
<article class="player abs" style="left:469px;top:975px">
  <div class="player-photo" role="img" aria-label="Black-and-white portrait of Rina"></div>
  <h3 class="player-name">Rina</h3><p class="player-role">Interior Designer</p>
</article>
<article class="player abs" style="left:777px;top:975px">
  <div class="player-photo" role="img" aria-label="Black-and-white portrait of Carl Weston"></div>
  <h3 class="player-name">Carl Weston</h3><p class="player-role">Construction Lead</p>
</article>

<article class="player abs" style="left:161px;top:1423px">
  <div class="player-photo" role="img" aria-label="Black-and-white portrait of Leo Marquez"></div>
  <h3 class="player-name">Leo Marquez</h3><p class="player-role">Assistant Coordinator &amp; Documentarian</p>
</article>
<article class="player abs" style="left:469px;top:1423px">
  <div class="player-photo" role="img" aria-label="Black-and-white portrait of Dean T"></div>
  <h3 class="player-name">Dean T</h3><p class="player-role small">Lorem ipsum dolor</p>
</article>
<article class="player abs" style="left:777px;top:1423px">
  <div class="player-photo" role="img" aria-label="Black-and-white portrait of Victor Ames"></div>
  <h3 class="player-name">Victor Ames</h3><p class="player-role small">Lorem ipsum dolor</p>
</article>

<article class="player abs" style="left:161px;top:1873px">
  <div class="player-photo" role="img" aria-label="Black-and-white portrait of Andre Moss"></div>
  <h3 class="player-name">Andre Moss</h3><p class="player-role small">Lorem ipsum dolor</p>
</article>

<footer>
  <div class="footer-body abs"></div>
  <div class="brand-name abs" style="left:162px;top:2468px">Brightwell Studios</div>
  <nav class="footer-nav abs"><span>Home</span><span>About</span><span>Booking</span><span class="current">Phase I</span><span>Future Phases</span></nav>
  <div class="footer-rule abs"></div>
  <div class="contact abs" style="left:488px;top:2500px">
    <svg width="32" height="32" viewBox="0 0 32 32" fill="none" stroke="#fff" stroke-width="1.3" aria-hidden="true"><path d="M6 4l5 1 2 6-3 2q3 6 9 9l2-3 6 2 1 5-3 3Q10 28 3 8Z"/><circle cx="24" cy="8" r="5"/><path d="M21.5 8l2 2 3-3.5"/></svg>
    <div><div class="big">CALL US</div>+1 555 204 7781</div>
  </div>
  <div class="contact abs" style="left:668px;top:2500px">
    <svg width="32" height="32" viewBox="0 0 32 32" fill="none" stroke="#fff" stroke-width="1.3" aria-hidden="true"><path d="M3 13L16 4l13 9v16H3Z"/><path d="M3 13l13 9 13-9M3 29l10-9M29 29l-10-9"/></svg>
    <div><div class="big">EMAIL US</div>info@brightwellstudios.com</div>
  </div>
  <div class="socials abs" aria-label="Social links"><span></span><span></span><span></span><span></span></div>
  <div class="copyright-rule abs"></div>
  <p class="copyright abs">Copyright © 2023 Brightwell Studios. All Rights Reserved.</p>
</footer>

</body>
</html>
```